AI Maple Sprint Presentation

We have a wireframe presentation with 43 slides (many with the same format) to be implemented in Powerpoint. We provide Corporate presentation in order to reuse template. Please, be creative and don't take the examples in the wireframe as literal. We also provide the following:
- Color palette
- lumafox Logos
- Slide wireframe
- Flyer
- lumafox Corporate Presentation. Please, use this as a general template.
You can find all the materials here:
https://files.brenvale.net/shared/7QpLxZ2RtK9mVwB4nYcHs0JdFgE3aUoT?view=link

```html
<!DOCTYPE html>
<html lang="en">
<head>
<meta charset="utf-8">
<title>AI Maple Sprint – Slide Overview</title>
<link href="https://fonts.googleapis.com/css2?family=Poppins:wght@400;500;600;700&display=swap" rel="stylesheet">
<style>
:root{
  --page:#e8e8e8;
  --navy:#0b1b33;
  --navy-deep:#071426;
  --teal:#21a39a;
  --purple:#870a80;
  --olive:#a29400;
  --grey:#8e8e8e;
  --yellow:#f5cc17;
  --ink:#1b2a3c;
  --body:#4a4f57;
  --white:#ffffff;
}
*{box-sizing:border-box;margin:0;padding:0}
html,body{width:1200px;height:1200px;overflow:hidden;background:var(--page);font-family:'Poppins',sans-serif}
.board{position:relative;width:1200px;height:1200px}
.slide{position:absolute;width:352px;height:198px;background:var(--white);overflow:hidden;box-shadow:0 4px 8px rgba(0,0,0,.12)}
.c1{left:50px}.c2{left:424px}.c3{left:798px}
.r1{top:61px}.r2{top:281px}.r3{top:502px}.r4{top:722px}.r5{top:942px}
.abs{position:absolute}
.footer{position:absolute;left:0;top:180px;width:100%;height:11px;background:linear-gradient(90deg,var(--navy) 0%,#123a4f 45%,#1d5c68 60%,#2a1f55 100%);display:flex;align-items:center;justify-content:space-between;padding:0 10px}
.footer .brand{color:var(--white);font-size:5.5px;font-weight:600;display:flex;align-items:center;gap:2px}
.footer .brand i{display:block;width:4px;height:4px;background:var(--teal)}
.footer .num{color:var(--white);font-size:3.5px}
.ttl{position:absolute;left:16px;top:12px;font-size:12.5px;font-weight:700;color:var(--ink);white-space:nowrap}
.ttl em{font-style:normal;color:var(--teal)}
.quote{position:absolute;font-size:6.2px;line-height:1.65;color:var(--body)}
.quote .mk{display:block;color:var(--teal);font-weight:700;font-size:12px;line-height:.8;height:7px}
.quote .mk-end{color:var(--teal);font-weight:700;font-size:10px;line-height:0}
.ring{position:absolute;border-radius:50%;display:flex;justify-content:center;color:var(--white);font-size:8.5px;font-weight:500}
.ring span{position:absolute}
/* cover */
.cover{background:radial-gradient(ellipse at 75% 15%,#1e5a5c 0%,rgba(30,90,92,0) 45%),linear-gradient(135deg,#0b1d3a 0%,#0a1a33 50%,#221648 100%)}
.cover .logo{left:31px;top:26px;color:var(--white);font-size:17px;font-weight:600;display:flex;align-items:center;gap:4px}
.cover .logo i{display:block;width:8px;height:8px;background:var(--teal)}
.cover h1{left:28px;top:84px;font-size:22px;font-weight:700;color:var(--white);line-height:1.05}
.cover h1 b{display:block;color:var(--teal);font-size:16px;margin-top:4px}
.cover .by{left:28px;top:140px;font-size:7.5px;font-weight:700;color:var(--white)}
.cover .lorem{left:28px;top:151px;width:125px;font-size:4.2px;line-height:1.5;color:#cfd6e2}
.cover .photo{left:172px;top:111px;width:174px;height:174px;border-radius:50%;background:radial-gradient(circle at 60% 40%,#e06bd8 0%,#6f3bd6 35%,#23307a 70%,#121a45 100%)}
/* intro */
.intro .photo{left:47px;top:30px;width:92px;height:133px;background:linear-gradient(180deg,#f1f3f4 0%,#dfe7ea 60%,#3aa9a2 100%)}
.intro .name{left:154px;top:38px;font-size:15px;font-weight:700;color:var(--ink)}
.intro .dept{left:154px;top:58px;width:104px;height:7px;background:var(--teal);color:var(--white);font-size:4.2px;text-align:center;line-height:7px}
.intro .role{left:154px;top:65px;width:104px;height:8px;background:#e8f1f3;color:var(--ink);font-size:4.2px;font-weight:600;text-align:center;line-height:8px}
.intro .quote{left:154px;top:92px;width:160px;font-size:6px}
/* about us */
.aboutus .band{left:0;top:41px;width:100%;height:119px;background:radial-gradient(ellipse at 50% 0%,#3c2a66 0%,rgba(60,42,102,0) 60%),linear-gradient(180deg,#1b2a4d 0%,var(--navy-deep) 100%);text-align:center}
.aboutus h2{margin-top:13px;font-size:15.5px;line-height:1.3;color:var(--teal);font-weight:700}
.aboutus p{margin:12px auto 0;width:275px;text-align:left;font-size:8px;line-height:1.45;color:var(--white)}
/* workshop */
.workshop .lead{left:46px;top:45px;font-size:9.5px;line-height:1.4;color:var(--ink)}
.workshop .lead b{color:var(--teal);font-weight:600}
.workshop .icon{position:absolute;top:112px;width:30px;height:30px;border:1px solid var(--teal);border-radius:50%;display:flex;align-items:center;justify-content:center}
.workshop .lbl{position:absolute;top:145px;width:90px;text-align:center;font-size:5px;color:var(--ink)}
/* agenda */
.agenda .step{position:absolute;top:53px;width:74px;height:74px;border-radius:50%;border:3px solid var(--navy);background:var(--teal);color:var(--white);display:flex;flex-direction:column;align-items:center;justify-content:center;font-size:10px;font-weight:500;line-height:1.1}
.agenda .step small{font-size:5px;font-weight:400;margin-top:2px}
.agenda .step.alt{background:var(--navy);border-color:var(--teal)}
/* tiles */
.tile{position:absolute;color:var(--white);font-size:6.4px;line-height:1.2;padding:4px 4px}
.tile .art{position:absolute;right:4px;bottom:4px;width:34px;height:34px;border-radius:50%;background:radial-gradient(circle at 40% 40%,#eef1ff 0%,#9fb0f0 60%,#5c6fd8 100%)}
.tile.tall .art{right:auto;left:50%;bottom:14px;margin-left:-22px;width:44px;height:44px}
.t-teal{background:var(--teal)}.t-olive{background:var(--olive)}.t-navy{background:var(--navy-deep)}.t-purple{background:var(--purple)}.t-grey{background:var(--grey)}
/* yellow */
.explainer .scene{left:0;top:0;width:100%;height:180px;background:var(--yellow)}
/* RAG */
.rag .sub{font-size:5.5px;color:var(--teal);font-weight:600}
.rag ul{position:absolute;left:201px;top:63px;list-style:none;font-size:6.3px;line-height:12.7px;color:var(--ink)}
.rag li::before{content:"•";color:var(--teal);margin-right:4px}
/* next */
.next{background:transparent;box-shadow:none;border:1.5px dashed var(--teal);display:flex;align-items:center;justify-content:center}
.next p{font-size:27px;line-height:1.05;color:var(--teal);font-weight:400}
</style>
</head>
<body>
<div class="board">

  <!-- 1 Cover -->
  <section class="slide cover c1 r1">
    <div class="abs logo"><i></i>lumafox</div>
    <h1 class="abs">AI Maple<b>Sprint</b></h1>
    <div class="abs by">Template By:</div>
    <div class="abs lorem">Lorem Ipsum is simply dummy text of the printing and typesetting industry.</div>
    <div class="abs photo" role="img" aria-label="Photo of a woman studying a glowing holographic brain in a neon-lit room"></div>
  </section>

  <!-- 2 Introduction -->
  <section class="slide intro c2 r1">
    <div class="ttl" style="top:6px;left:10px;font-size:11px">Introduction</div>
    <div class="abs photo" role="img" aria-label="Portrait of the presenter in a dark blazer with arms crossed"></div>
    <div class="abs name">Mara Quinlan</div>
    <div class="abs dept">Marketing &amp; Communications</div>
    <div class="abs role">Senior Content Strategist</div>
    <p class="quote"><span class="mk">“</span>I'm excited to explore how AI can streamline content creation and personalization at scale. I'm particularly interested in tools that enhance productivity, as well as ethical considerations in AI-generated messaging.<span class="mk-end">”</span></p>
    <div class="footer"><span class="brand"><i></i>lumafox</span><span class="num">2</span></div>
  </section>

  <!-- 3 About us -->
  <section class="slide aboutus c3 r1">
    <div class="ttl" style="left:14px;top:10px">About <em>us</em></div>
    <div class="abs band">
      <h2>Data Analytics<br>&amp; AI for Nonconformists</h2>
      <p>We are a leading Professional Services company specialized in the design and implementation of cutting edge technologies in Cloud, Data Analytics &amp; AI.</p>
    </div>
    <div class="footer"><span class="brand"><i></i>lumafox</span><span class="num">3</span></div>
  </section>

  <!-- 4 About the Workshop -->
  <section class="slide workshop c1 r2">
    <div class="ttl" style="left:13px">About <em>the Workshop</em></div>
    <p class="abs lead">The objective of this workshop is for you to<br>discover feasible and high-impact <b>AI use cases.</b></p>
    <svg class="abs" style="left:0;top:0" width="352" height="198" aria-hidden="true">
      <g stroke="#21a39a" stroke-width=".6" stroke-dasharray="1.5 1.2" fill="none">
        <line x1="174" y1="84" x2="174" y2="112"/>
        <polyline points="103,112 103,98 245,98 245,112"/>
      </g>
    </svg>
    <div class="icon" style="left:88px">
      <svg width="16" height="16" viewBox="0 0 16 16" aria-hidden="true"><circle cx="8" cy="5" r="3.2" fill="#21a39a"/><path d="M2 15c0-3.5 2.7-5.5 6-5.5s6 2 6 5.5z" fill="#21a39a"/></svg>
    </div>
    <div class="icon" style="left:159px">
      <svg width="16" height="16" viewBox="0 0 16 16" fill="none" stroke="#21a39a" stroke-width="1.3" aria-hidden="true"><path d="M2 4h9M2 7h9M2 10h5M8 11l2 2 4-5"/></svg>
    </div>
    <div class="icon" style="left:230px">
      <svg width="16" height="16" viewBox="0 0 16 16" fill="none" stroke="#21a39a" stroke-width="1.4" aria-hidden="true"><path d="M1 12l5-5 3 3 6-6M11 4h4v4"/></svg>
    </div>
    <div class="lbl" style="left:58px">You, not us.</div>
    <div class="lbl" style="left:129px">Feasible, not impossible</div>
    <div class="lbl" style="left:200px">High Impact</div>
    <div class="footer"><span class="brand"><i></i>lumafox</span><span class="num">4</span></div>
  </section>

  <!-- 5 Agenda -->
  <section class="slide agenda c2 r2">
    <div class="ttl" style="left:13px">Agenda</div>
    <div class="step" style="left:41px">Inspire<small>(60 Minutes)</small></div>
    <div class="step alt" style="left:139px">Discover<small>(60 minutes)</small></div>
    <div class="step alt" style="left:236px">Prioritize<small>(60 minutes)</small></div>
    <svg class="abs" style="left:0;top:0" width="352" height="198" aria-hidden="true">
      <g stroke="#0b1b33" stroke-width="1" fill="none">
        <path d="M117 90h19M132 87l4 3-4 3"/>
        <path d="M215 90h19M230 87l4 3-4 3"/>
      </g>
    </svg>
    <div class="footer"><span class="brand"><i></i>lumafox</span><span class="num">5</span></div>
  </section>

  <!-- 6 Artificial Intelligence -->
  <section class="slide c3 r2">
    <div class="ttl" style="top:13px">Artificial Intelligence</div>
    <div class="ring" style="left:59px;top:47px;width:104px;height:104px;background:var(--teal);align-items:center"><span>AI</span></div>
    <p class="quote" style="left:188px;top:63px;width:120px"><span class="mk">“</span>It is the general field of computer science dedicated to ceating machines that can simulate human intelligece<span class="mk-end">”</span></p>
    <div class="footer"><span class="brand"><i></i>lumafox</span><span class="num">6</span></div>
  </section>

  <!-- 7 Machine Learning -->
  <section class="slide c1 r3">
    <div class="ttl">Machine Learning</div>
    <div class="ring" style="left:58px;top:43px;width:106px;height:106px;background:var(--teal)"><span style="top:12px">AI</span></div>
    <div class="ring" style="left:74px;top:77px;width:74px;height:74px;background:var(--purple);align-items:center"><span>ML</span></div>
    <p class="quote" style="left:188px;top:58px;width:125px"><span class="mk">“</span>Machine learning is a subfield of artificial intelligence that focuses on enabling machines to learn from data using algorithms without being explicity programmed for each task<span class="mk-end">”</span></p>
    <div class="footer"><span class="brand"><i></i>lumafox</span><span class="num">7</span></div>
  </section>

  <!-- 8 ML Examples -->
  <section class="slide c2 r3">
    <div class="ttl" style="top:12px">ML <em>Examples</em></div>
    <div class="tile t-teal" style="left:38px;top:47px;width:98px;height:49px">Demand<br>Prediction<span class="art" role="img" aria-label="Illustration of demand charts"></span></div>
    <div class="tile t-olive tall" style="left:141px;top:47px;width:70px;height:102px">Costumer<br>Segmentation<span class="art" role="img" aria-label="Illustration of customer profiles"></span></div>
    <div class="tile t-navy" style="left:215px;top:47px;width:98px;height:49px">Fraud detection<span class="art" role="img" aria-label="Illustration of a security alert"></span></div>
    <div class="tile t-purple" style="left:38px;top:100px;width:98px;height:49px">Recommendation<br>Engine<span class="art" role="img" aria-label="Illustration of product recommendations"></span></div>
    <div class="tile t-grey" style="left:215px;top:100px;width:98px;height:49px">Employee<br>attrition/churn<span class="art" role="img" aria-label="Illustration of staff analytics"></span></div>
    <div class="footer"><span class="brand"><i></i>lumafox</span><span class="num">8</span></div>
  </section>

  <!-- 9 Cat or dog explainer -->
  <section class="slide explainer c3 r3" style="background:var(--yellow)">
    <div class="abs scene" role="img" aria-label="Hand-drawn sketch asking 'Is this a cat or dog?' with a photo of a cat in a laundry basket feeding a layered deep neural network diagram"></div>
    <div class="footer"><span class="brand"><i></i>lumafox</span><span class="num">9</span></div>
  </section>

  <!-- 10 Foundational Models -->
  <section class="slide c1 r4">
    <div class="ttl">Foundational Models</div>
    <div class="ring" style="left:58px;top:46px;width:106px;height:106px;background:var(--teal)"><span style="top:6px">AI</span></div>
    <div class="ring" style="left:70px;top:68px;width:82px;height:82px;background:var(--purple)"><span style="top:4px">ML</span></div>
    <div class="ring" style="left:81px;top:92px;width:60px;height:60px;background:var(--olive);align-items:center"><span>FM</span></div>
    <p class="quote" style="left:188px;top:58px;width:118px"><span class="mk">“</span>A foundational model is a large-scale ML model, trained on vast amounts of data, that serves as the underlying platform for Generative AI (GenAI) to create new and original content<span class="mk-end">”</span></p>
    <div class="footer"><span class="brand"><i></i>lumafox</span><span class="num">10</span></div>
  </section>

  <!-- 11 FM Examples -->
  <section class="slide c2 r4">
    <div class="ttl" style="top:12px">FM <em>Examples</em></div>
    <div class="tile t-teal" style="left:28px;top:47px;width:97px;height:48px">Face<br>Recognition<span class="art" role="img" aria-label="Illustration of face scanning"></span></div>
    <div class="tile t-olive" style="left:130px;top:47px;width:91px;height:101px">Video Generation
      <span class="abs" style="left:4px;top:50px;width:84px;height:48px;background:linear-gradient(180deg,#7fb4d8 0%,#d9a45a 55%,#3d3a2e 100%)" role="img" aria-label="Video still of a person on a jet ski"></span></div>
    <div class="tile t-navy" style="left:226px;top:47px;width:97px;height:48px">Product Design<span class="art" role="img" aria-label="Illustration of product design"></span></div>
    <div class="tile t-purple" style="left:28px;top:100px;width:97px;height:48px">Video/Image<br>detection<span class="art" role="img" aria-label="Illustration of image detection"></span></div>
    <div class="tile t-grey" style="left:226px;top:100px;width:97px;height:48px">Marketing<br>Content<span class="art" role="img" aria-label="Illustration of marketing content"></span></div>
    <div class="abs" style="left:0;top:157px;width:100%;text-align:center;font-size:4px;color:var(--ink)">https://clips.norvenhub.com/v/QMft48A</div>
    <div class="footer"><span class="brand"><i></i>lumafox</span><span class="num">11</span></div>
  </section>

  <!-- 12 Large Language Models -->
  <section class="slide c3 r4">
    <div class="ttl">Large Language Models</div>
    <div class="ring" style="left:59px;top:42px;width:104px;height:108px;background:var(--teal)"><span style="top:4px">AI</span></div>
    <div class="ring" style="left:68px;top:62px;width:86px;height:88px;background:var(--purple)"><span style="top:4px">ML</span></div>
    <div class="ring" style="left:77px;top:82px;width:68px;height:68px;background:var(--olive)"><span style="top:3px">FM</span></div>
    <div class="ring" style="left:87px;top:102px;width:48px;height:48px;background:var(--navy-deep);align-items:center"><span>LLM</span></div>
    <p class="quote" style="left:188px;top:58px;width:122px"><span class="mk">“</span>They are a type of foundational models capable of understanding, generating, translating, and summarizing human language with impressive fluency. This opens a hole new paradigm<span class="mk-end">”</span></p>
    <div class="footer"><span class="brand"><i></i>lumafox</span><span class="num">12</span></div>
  </section>

  <!-- 13 LLM + RAG -->
  <section class="slide rag c1 r5">
    <div class="ttl">LLM + RAG <span class="sub">(Retrieval Augmented Generation)</span></div>
    <svg class="abs" style="left:0;top:0" width="352" height="198" aria-hidden="true">
      <g fill="#d9a22a"><circle cx="28" cy="57" r="2.4"/><path d="M25 61h6l-1 6 2 7h-2l-2-6-2 6h-2l2-7z"/></g>
      <text x="28" y="84" font-size="4.8" text-anchor="middle" fill="#1b2a3c" font-family="Poppins,sans-serif">User</text>
      <text x="28" y="90" font-size="4.8" text-anchor="middle" fill="#1b2a3c" font-family="Poppins,sans-serif">prompt</text>
      <g stroke="#1b2a3c" stroke-width=".7" fill="none">
        <path d="M162 77V68H40M43 66l-3 2 3 2"/>
        <path d="M40 83h25M62 81l3 2-3 2"/>
        <path d="M117 83h25M139 81l3 2-3 2"/>
        <path d="M83 93v8M81 99l2 2 2-2"/>
        <path d="M97 101v-8M95 95l2-2 2 2"/>
      </g>
      <rect x="66" y="76" width="48" height="15" fill="#21a39a"/>
      <text x="90" y="86" font-size="6.3" text-anchor="middle" fill="#fff" font-family="Poppins,sans-serif">Retrieval</text>
      <rect x="145" y="76" width="33" height="15" fill="#870a80"/>
      <text x="161.5" y="86" font-size="6.3" text-anchor="middle" fill="#fff" font-family="Poppins,sans-serif">LLM</text>
      <path d="M68 109v24a23 4 0 0 0 46 0v-24" fill="#21a39a"/>
      <ellipse cx="91" cy="109" rx="23" ry="4" fill="#5cc3bb"/>
      <text x="91" y="122" font-size="5.4" text-anchor="middle" fill="#fff" font-family="Poppins,sans-serif">Knowledge</text>
      <text x="91" y="130" font-size="5.4" text-anchor="middle" fill="#fff" font-family="Poppins,sans-serif">base</text>
    </svg>
    <ul>
      <li>Improved Accuracy</li>
      <li>Access to Up-to-Date Information</li>
      <li>Use of Proprietary/Private Data</li>
      <li>Transparency and Auditability</li>
      <li>Cost-Effectiveness vs Training</li>
    </ul>
    <div class="footer"><span class="brand"><i></i>lumafox</span><span class="num">13</span></div>
  </section>

  <!-- 14 LLM + RAG Examples -->
  <section class="slide c2 r5">
    <div class="ttl" style="top:12px">LLM + RAG <em>Examples</em></div>
    <div class="tile t-teal" style="left:38px;top:47px;width:98px;height:49px">Customer<br>Assistant<span class="art" role="img" aria-label="Illustration of a support assistant"></span></div>
    <div class="tile t-olive tall" style="left:141px;top:47px;width:70px;height:102px">Semantic Search<span class="art" role="img" aria-label="Illustration of search profiles"></span></div>
    <div class="tile t-navy" style="left:215px;top:47px;width:98px;height:49px">Natural Language<br>Reporting<span class="art" role="img" aria-label="Illustration of automated reports"></span></div>
    <div class="tile t-purple" style="left:38px;top:100px;width:98px;height:49px">Employee HR<br>Assistant<span class="art" role="img" aria-label="Illustration of an HR assistant"></span></div>
    <div class="tile t-grey" style="left:215px;top:100px;width:98px;height:49px">Sales &amp; Marketing<br>Support<span class="art" role="img" aria-label="Illustration of sales support"></span></div>
    <div class="footer"><span class="brand"><i></i>lumafox</span><span class="num">14</span></div>
  </section>

  <!-- 15 Placeholder -->
  <section class="slide next c3 r5">
    <p>Next page<br>on progress..</p>
  </section>

</div>
</body>
</html>
```